WebDesign Flyer - A5 Double Sided

We create a complete web presence for local businesses.
A comprehensive background on our services and company can be found at www.brightnetstall.co.uk and on the attached sales document.

We want these flyers (a5, double sided, colour) to portray us as a local, professional and friendly service that will take care fully of a business's online presence. This includes website, hosting, email, domain AND IMPORTANTLY: we also can build them a business profile on business directory websites such as PinTown, OurCornerHub, Vistamap Spots, Quib etc. which helps them increase their profit.

Target Market(s)

Small to medium businesses found on the high street. eg: restaurants, physios, doctors, retail shops, salons, hairdressers, as well as more corporate businesses like accountancy firms and lawyers.

Industry/Entity Type

Business Directory

Requirements
Must have
• Full project files provided with all required elements if design is chosen. Design to mention: sites can be updated in less than 1 minute in 3 clicks, No contracts, money back guarantee (no risk), prices from £400, SEO as standard, brightnetstall.co.uk, 020 7946 0381, info@brightnetstall.co.uk, 10% discount with this flyer until December 20th 2010.
Nice to have
• To mention: dedicated support, business photos (see brightnetstall.co.uk/features), Chatterly, Peepline, ReelBox, Snapvault, CareerMesh Integration, free consultation, logos of services we provide (see logos.zip for examples).
Should not have
• our logo featured too prominently.

```html
<!DOCTYPE html>
<html lang="en">
<head>
<meta charset="utf-8">
<title>Bright Net Stall – What we do</title>
<link rel="stylesheet" href="https://fonts.googleapis.com/css2?family=Cinzel:wght@900&family=Cabin:wght@400;700&display=swap">
<style>
  :root {
    --sky-top: #6fb6ec;
    --sky-mid: #2f76c2;
    --sky-deep: #0a2550;
    --panel: #ffffff;
    --ink: #111111;
    --label: #111111;
    --glow: #fff36a;
    --glow-soft: rgba(255, 243, 106, 0.45);
    --cursor-line: #8a8a8a;
    --site-orange: #e8922c;
    --site-cream: #f6ecd0;
    --site-wood: #b98a55;
    --site-lilac: #d9c6e6;
    --site-lime: #eef3a8;
    --site-navy: #1a2f6a;
    --site-stone: #e9e9e6;
    --brand: #1b62c4;
    --brand-dot: #ffd21f;
  }
  * { box-sizing: border-box; margin: 0; padding: 0; }
  html, body { width: 846px; height: 1200px; overflow: hidden; }
  body {
    position: relative;
    background: linear-gradient(180deg, var(--sky-top) 0%, var(--sky-mid) 45%, var(--sky-deep) 100%);
    font-family: "Cabin", "Gill Sans", sans-serif;
    color: var(--ink);
  }
  .panel {
    position: absolute; left: 57px; top: 57px; width: 733px; height: 1086px;
    background: var(--panel); border-radius: 14px; overflow: hidden;
  }
  .panel__glow {
    position: absolute; left: 300px; top: 0; width: 433px; height: 560px;
    background: radial-gradient(ellipse at 55% 45%, var(--glow-soft) 0%, rgba(255,243,106,0.18) 55%, rgba(255,255,255,0) 75%);
  }
  .panel__glow--left {
    left: 20px; top: 120px; width: 300px; height: 520px;
    background: radial-gradient(ellipse at 50% 50%, rgba(255,243,106,0.3) 0%, rgba(255,255,255,0) 70%);
  }
  .heading {
    position: absolute; font-family: "Cinzel", serif; font-weight: 900;
    font-size: 34px; line-height: 1; color: var(--ink);
    text-shadow: 3px 3px 0 rgba(0,0,0,0.25);
  }
  .heading--what { left: 88px; top: 86px; padding-bottom: 4px; border-bottom: 2px solid var(--ink); }
  .heading--contact { right: 84px; top: 564px; }
  .heading--works { left: 50px; top: 752px; transform: rotate(-8deg); transform-origin: left center; }

  .side-label {
    position: absolute; font-family: "Cabin", sans-serif; font-weight: 700;
    font-size: 24px; line-height: 0.95; color: var(--label);
    transform: rotate(-90deg); transform-origin: left top; text-align: center;
  }
  .side-label--website { left: 90px; top: 262px; }
  .side-label--online { left: 452px; top: 268px; }
  .side-label--social { left: 72px; top: 503px; }
  .side-label--peace { left: 474px; top: 516px; }

  .service-list { position: absolute; list-style: none; }
  .service-list li {
    font-weight: 700; font-variant: small-caps; font-size: 21px; line-height: 0.98;
    letter-spacing: 0.2px;
  }
  .service-list li small { font-size: 21px; display: block; }
  .service-list--website { left: 123px; top: 135px; }
  .service-list--website li { margin-bottom: 17px; }
  .service-list--online { left: 506px; top: 135px; }
  .service-list--online li { margin-bottom: 12px; }
  .service-list--social { left: 123px; top: 319px; }
  .service-list--social li { margin-bottom: 16px; }
  .service-list--peace { left: 506px; top: 319px; }
  .service-list--peace li { margin-bottom: 14px; }

  .contact { position: absolute; right: 84px; top: 613px; text-align: right; font-size: 23px; line-height: 30px; }
  .contact dt { display: inline; font-weight: 700; font-variant: small-caps; }
  .contact dd { display: inline; }
  .contact__row { display: block; }

  .cursors { position: absolute; left: 80px; top: 552px; }

  .work {
    position: absolute; box-shadow: 2px 3px 8px rgba(0,0,0,0.45);
  }
  .work--restaurant {
    left: 285px; top: 712px; width: 495px; height: 228px;
    background: linear-gradient(180deg, var(--site-orange), #d97a1c);
    transform: rotate(-2deg);
  }
  .work--restaurant::after {
    content: ""; position: absolute; left: 82px; top: 28px; width: 340px; height: 200px;
    background: var(--site-cream); border-radius: 10px 10px 0 0;
  }
  .work--shoes {
    left: 55px; top: 792px; width: 305px; height: 345px;
    background: linear-gradient(180deg, var(--site-wood) 0%, #7a4f30 40%, #f2eee8 45%, #f2eee8 100%);
    transform: rotate(-4deg);
  }
  .work--pizzeria {
    left: 385px; top: 843px; width: 405px; height: 297px;
    background: linear-gradient(180deg, var(--site-navy) 0%, var(--site-navy) 6%, var(--site-stone) 6%, #cfcfcb 100%);
  }
  .work--salon {
    left: 163px; top: 938px; width: 432px; height: 215px;
    background: linear-gradient(180deg, var(--site-lilac), #cdb4de);
    transform: rotate(-2.5deg);
  }
  .work--salon::after {
    content: ""; position: absolute; left: 28px; top: 14px; width: 380px; height: 200px;
    background: linear-gradient(180deg, var(--site-lime) 0%, #f4f6c8 40%, #fbfbe6 100%);
    border-radius: 10px 10px 0 0;
  }

  .brand {
    position: absolute; left: 572px; top: 1058px; width: 195px; height: 66px;
    background: var(--panel); display: flex; align-items: center; gap: 8px; padding: 0 10px;
    border-radius: 6px;
  }
  .brand__dot { width: 18px; height: 18px; border-radius: 50%; background: var(--brand-dot); flex: none; }
  .brand__name { font-family: "Cabin", sans-serif; font-weight: 700; font-size: 22px; color: var(--brand); line-height: 1; }
</style>
</head>
<body>
  <main class="panel">
    <div class="panel__glow" role="img" aria-label="Soft yellow upward arrows rising behind the services"></div>
    <div class="panel__glow panel__glow--left" role="img" aria-label="Soft yellow upward arrows rising behind the services"></div>
  </main>

  <h2 class="heading heading--what">What we do:</h2>

  <span class="side-label side-label--website" style="width:128px">WEBSITE</span>
  <ul class="service-list service-list--website">
    <li>Website built from scratch</li>
    <li>Content Management System</li>
    <li>Professional Business Photos</li>
    <li>Gloobe Analytics</li>
  </ul>

  <span class="side-label side-label--online" style="width:135px">ONLINE<br>PRESENCE</span>
  <ul class="service-list service-list--online">
    <li>Search Engine Optimisation</li>
    <li>Gloobe Maps Registration</li>
    <li>News and Blog Feed<small>Syndication</small></li>
    <li>Business Listings</li>
  </ul>

  <span class="side-label side-label--social" style="width:160px">SOCIAL MEDIA<br>PRESENCE</span>
  <ul class="service-list service-list--social">
    <li>Chatterly Page</li>
    <li>Peepline for promotion<small>and updates</small></li>
    <li>CareerMesh for the exchange<small>of ideas and opportunities</small></li>
    <li>ReelBox for video promotion<small>and business value</small></li>
  </ul>

  <span class="side-label side-label--peace" style="width:182px">PEACE OF MIND</span>
  <ul class="service-list service-list--peace">
    <li>No Contracts means<small>no commitment</small></li>
    <li>100% Satisfaction<small>or your money back</small></li>
    <li>Virus Protection<small>to keep your site safe</small></li>
    <li>Technical Support to help<small>you manage your website</small></li>
  </ul>

  <svg class="cursors" width="270" height="150" viewBox="0 0 270 150" aria-hidden="true">
    <g fill="none" stroke-linejoin="round" stroke-width="3">
      <path d="M20 20 L20 140 L45 115 L60 148 L72 142 L58 110 L92 108 Z" stroke="#d8d8d8" transform="translate(-10,0)"/>
      <path d="M20 20 L20 140 L45 115 L60 148 L72 142 L58 110 L92 108 Z" stroke="#c4c4c4" transform="translate(35,-5)"/>
      <path d="M20 20 L20 140 L45 115 L60 148 L72 142 L58 110 L92 108 Z" stroke="#a8a8a8" transform="translate(80,-10)"/>
      <path d="M20 20 L20 140 L45 115 L60 148 L72 142 L58 110 L92 108 Z" stroke="var(--cursor-line)" transform="translate(125,-14)"/>
      <path d="M20 20 L20 140 L45 115 L60 148 L72 142 L58 110 L92 108 Z" fill="#fff" stroke="#000" stroke-width="4" transform="rotate(30 190 80) translate(150,-10)"/>
    </g>
  </svg>

  <h2 class="heading heading--contact">Contact</h2>
  <dl class="contact">
    <span class="contact__row"><dt>Phone:</dt> <dd>020 7946 0381</dd></span>
    <span class="contact__row"><dt>E-mail:</dt> <dd>info@brightnetstall.co.uk</dd></span>
    <span class="contact__row"><dt>Web:</dt> <dd>http://brightnetstall.co.uk</dd></span>
  </dl>

  <div class="work work--restaurant" role="img" aria-label="Screenshot of a restaurant website with orange frame and cream page"></div>
  <div class="work work--shoes" role="img" aria-label="Screenshot of a boot shop website with wooden header and boot photo"></div>
  <div class="work work--pizzeria" role="img" aria-label="Screenshot of a pizzeria website showing the restaurant front"></div>
  <div class="work work--salon" role="img" aria-label="Screenshot of a hair salon website with lilac frame and lime header"></div>

  <h2 class="heading heading--works">Our works:</h2>

  <div class="brand">
    <span class="brand__dot"></span>
    <span class="brand__name">Bright Net Stall</span>
  </div>
</body>
</html>
```